Banner Ad Design Project

We need a server banner image for our web site. The banner is to sell dedicated servers. The size needs to be 732x138 pixels.

Here is an example of the background we're thinking about: http://www.quolventa.com/images/banners/qvbanner.png

But feel free to be creative, and design a banner that looks good on the following page: http://www.quolventa.com/marbexservers.asp

Incorporate some of these words in the banner as features:
-Rapid I/O SSD Hybrid RAID
-SLA Included
-Marbex Dorvo Processors
-24x7 Monitoring and Support

I like the colors on this banner... http://www.quolventa.com/images/banners/header-spring.png

so, maybe a white background would look good.

```html
<!DOCTYPE html>
<html lang="en">
<head>
<meta charset="utf-8">
<title>Dedicated Servers – SSD Hybrid RAID</title>
<link rel="stylesheet" href="https://fonts.googleapis.com/css2?family=PT+Sans+Narrow:wght@400;700&display=swap">
<style>
  :root {
    --bg-deep: #58628a;
    --bg-mid: #6f789c;
    --bg-light: #9199b8;
    --hardware-dark: #3e4560;
    --hardware-silver: #b9bfd3;
    --hardware-shine: #d8dce8;
    --text-light: #ffffff;
    --text-soft: #eef0f7;
  }
  * { margin: 0; padding: 0; box-sizing: border-box; }
  html, body {
    width: 1200px;
    height: 226px;
    overflow: hidden;
    background: #ffffff;
  }
  .banner {
    position: relative;
    width: 1200px;
    height: 226px;
    overflow: hidden;
    background: linear-gradient(90deg, var(--bg-deep) 0%, var(--bg-mid) 35%, var(--bg-light) 60%, var(--bg-mid) 100%);
    font-family: "PT Sans Narrow", "Arial Narrow", sans-serif;
    color: var(--text-light);
  }
  .hardware-visual {
    position: absolute;
    top: 0;
    right: 0;
    width: 700px;
    height: 226px;
    background:
      linear-gradient(90deg, var(--bg-light) 0%, rgba(145,153,184,0) 30%),
      linear-gradient(180deg,
        var(--hardware-dark) 0%,
        var(--hardware-silver) 14%,
        var(--hardware-shine) 30%,
        var(--hardware-dark) 46%,
        var(--hardware-dark) 52%,
        var(--hardware-silver) 64%,
        var(--hardware-shine) 80%,
        var(--hardware-dark) 100%);
  }
  .headline {
    position: absolute;
    left: 49px;
    top: 52px;
  }
  .headline-kicker {
    display: block;
    font-size: 37px;
    font-weight: 400;
    line-height: 1;
    color: var(--text-soft);
  }
  .headline-main {
    display: flex;
    align-items: baseline;
    margin-top: 8px;
  }
  .headline-product {
    font-size: 62px;
    font-weight: 700;
    line-height: 1;
    letter-spacing: 0.3px;
  }
  .headline-support {
    margin-left: 20px;
    font-size: 30px;
    font-weight: 400;
    color: var(--text-soft);
  }
</style>
</head>
<body>
  <div class="banner">
    <div class="hardware-visual" role="img" aria-label="Close-up of rack-mounted dedicated server units"></div>
    <div class="headline">
      <span class="headline-kicker">Dedicated Servers</span>
      <div class="headline-main">
        <span class="headline-product">SSD Hybrid RAID</span>
        <span class="headline-support">24x7 Support</span>
      </div>
    </div>
  </div>
</body>
</html>
```